HarborLoop - Shore Excursions Operator Software Trade show pop-up display

Create Trade show Pop-up banners Suitable for printing at 33.5 inches by 80 inches high. I have included a description of what our software does. We are at a trade show focusing on acquiring tour operators to sign up and use our software. This specifically is built for cruise line markets. I am uploading two versions of our logo, one is just a simple version the other is the name spelled out. We want to include both because as a new company the branding identity is not very strong with the simple logo. The image I'm uploading is a backdrop with the cruise ship is what we use for our back image on the customer facing website. I am also uploading some screenshots of our software which is designed for desktop, tablet, and mobile. I want to be provocative and enticing and somewhat cutting edge but certainly to be driven towards the cruise industry and tour operators who work with the cruise industry specifically. I also uploaded an example of a chatgpt display for reference as to what we are looking for (but not that image specifically).
HarborLoop Software Overview for Designers
Purpose of the Software:
HarborLoop is an all-in-one operating system for shore excursion tour operators. It connects directly with cruise lines, manages every part of tour operations, and helps operators maximize revenue while reducing manual work.
The software is designed for companies that provide tours, transportation, and shore excursions for cruise ship passengers. Operators use HarborLoop to run their entire business — from inventory management to daily dispatch.
Key Value in Simple Terms
Maximize Revenue → By syncing with cruise ship schedules, managing contracts, invoicing, and reallocating inventory in real time.
Operational Control → From assigning guides and vehicles to monitoring maintenance and scheduling daily tours automatically.
Simplify Bookings → Manage bookings from cruise lines, travel agents, and direct guests in one hub.
Smarter Management → Staff, inventory, contracts, and content are centralized for full visibility and efficiency.
Future-Proof → Analytics, reporting, and scalability ensure operators grow alongside cruise line demand.
What HarborLoop Does (Modules & Functions)
1. Cruise Line & Revenue Management
Real-time cruise calendars
Pricing & contract management
Automated invoicing for cruise lines
Faster release of inventory for sales
Visual cues for design: 📅 Calendar icons, 💰 revenue charts, 📄 contract documents.
2. Inventory & Allocation
Central hub for inventory (direct sales, cruise lines, individual ships)
Automatic capacity alerts (when seats run low)
Bulk uploads of sales data (hundreds of hours saved)
Demand-based allocation for higher yield
Visual cues: 🚍 Bus seats filling up, ⚠️ alerts, ⬆️ demand graphs.
3. Booking & Guest Management
Unified booking system (cruise lines, agents, direct guests)
Integrated payments & invoices
Guest management for changes, cancellations, special requests
Agent & affiliate campaign tools
Visual cues: 🎟 tickets, 🧑🤝🧑 guest icons, 💳 payment/booking screens.
4. Daily Tour Dispatch (DTD)
Generates real-time daily tour schedule
Assigns guides, drivers, and vehicles automatically
Tracks guest counts & departures live
Mobile access for staff & guides
Visual cues: 🚌 bus/tour icons, 📱 mobile access, ✅ checklist/schedule view.
5. Fleet & Maintenance
Live fleet tracking (location, activity, mileage)
Inspection & maintenance reports
Photo/video upload for repair tracking
Visual cues: 🚐 vehicles, 🔧 maintenance tools, 📍 GPS markers.
6. Employee & Staff Management
Track certifications, training, and staff profiles
Assign roles, shifts, and responsibilities
Proactive alerts for expired credentials
Visual cues: 🧑✈️ staff badges, 🎓 training icons, 👤 profile cards.
7. Content & Branding Control
Manage all tour content (descriptions, itineraries, FAQs, images, videos)
Apply refund policies & contracted rates
Ensure consistent, accurate guest-facing info
Visual cues: 🖼 images, 📝 itinerary lists, 🌐 consistent branding.
8. Analytics & Future-Proofing
Sales reporting by ship, departure, and channel
Historic vs. future pricing analysis
Scalable platform that grows with the operator
Visual cues: 📊 dashboards, 📈 performance charts, 🔮 forward-looking visuals.
Overall Design Themes to Convey
Smart, seamless, and connected. (No clutter, everything integrated.)
Professional + trustworthy. (Executive decision-makers are the audience.)
Cruise-specific but modern. (Avoid cliché palm trees; instead, ships, schedules, people, and data visuals.)
Dynamic and active. (Show energy — tours, departures, real-time control.)

```html
<!DOCTYPE html>
<html lang="en">
<head>
<meta charset="UTF-8">
<title>HarborLoop – The Operating System for Shore Excursions</title>
<link href="https://fonts.googleapis.com/css2?family=Roboto:wght@400;700;900&display=swap" rel="stylesheet">
<style>
  :root {
    --ocean-navy: #03408c;
    --deep-navy: #06397a;
    --ink-navy: #0b3566;
    --sky-light: #e4eefb;
    --accent-blue: #2fa4f0;
    --label-white: #eaf2ff;
    --headline-white: #f3f6ff;
    --device-black: #1b1c1f;
    --sunset-top: #e98a55;
    --sunset-mid: #f2b27d;
    --sea-teal: #2b7d99;
  }
  * { margin: 0; padding: 0; box-sizing: border-box; }
  html, body { width: 1200px; height: 2865px; overflow: hidden; }
  body { font-family: "Roboto", Arial, sans-serif; background: var(--ocean-navy); }

  .banner { position: relative; width: 1200px; height: 2865px; background: var(--ocean-navy); overflow: hidden; }

  .hero-scene { position: absolute; left: 0; top: 0; width: 1200px; height: 1040px; }

  .brand-mark {
    position: absolute; left: 66px; top: 66px;
    display: flex; align-items: center; gap: 14px;
    font-weight: 700; font-size: 44px; color: var(--ink-navy);
  }
  .brand-mark .dot { width: 26px; height: 26px; border-radius: 50%; background: var(--ink-navy); }

  .tablet-shadow {
    position: absolute; left: 360px; top: 1010px; width: 480px; height: 50px;
    border-radius: 50%; background: rgba(0, 20, 50, 0.55); filter: blur(18px);
  }
  .tablet {
    position: absolute; left: 317px; top: 623px; width: 573px; height: 391px;
    background: var(--device-black); border-radius: 32px; padding: 16px;
  }
  .tablet-screen {
    width: 100%; height: 100%; border-radius: 14px;
    background: linear-gradient(90deg, #123a55 0 13%, #f6f8fb 13% 100%);
  }

  .headline {
    position: absolute; left: 0; top: 1128px; width: 1200px;
    text-align: center; color: var(--headline-white);
    font-weight: 700; font-size: 106px; line-height: 94px; letter-spacing: -0.5px;
  }

  .values-tag {
    position: absolute; left: 445px; top: 1546px; width: 318px; height: 80px;
    background: #ffffff; border-radius: 16px;
    display: flex; align-items: center; justify-content: center;
    color: var(--ink-navy); font-weight: 700; font-size: 54px;
  }

  .value { position: absolute; width: 360px; text-align: center; }
  .value svg { display: block; margin: 0 auto; }
  .value-label {
    margin-top: 22px; color: var(--label-white);
    font-size: 38px; line-height: 54px; font-weight: 400;
  }
  .v-revenue { left: 92px; top: 1700px; }
  .v-control { left: 425px; top: 1700px; }
  .v-bookings { left: 756px; top: 1700px; }
  .v-management { left: 230px; top: 2028px; }
  .v-future { left: 596px; top: 2028px; }

  .deco-circle {
    position: absolute; left: 38px; top: 2300px; width: 164px; height: 164px;
    border-radius: 50%; background: var(--deep-navy);
  }

  .closing-arc {
    position: absolute; left: -260px; top: 2358px; width: 1720px; height: 1400px;
    border-radius: 50%; background: var(--sky-light);
  }
  .tagline {
    position: absolute; left: 0; top: 2505px; width: 1200px; text-align: center;
    color: var(--ink-navy); font-weight: 900; font-size: 64px; line-height: 60px;
  }
  .wordmark {
    position: absolute; left: 0; top: 2680px; width: 1200px; text-align: center;
    color: var(--ink-navy); font-weight: 900; font-size: 92px; letter-spacing: 2px;
  }
</style>
</head>
<body>
<div class="banner">

  <svg class="hero-scene" viewBox="0 0 1200 1040" role="img" aria-label="Photograph of a white cruise ship sailing on a turquoise sea under an orange sunset sky, with water splashes">
    <defs>
      <linearGradient id="sceneGradient" x1="0" y1="0" x2="0" y2="1">
        <stop offset="0" stop-color="#c98a6c"/>
        <stop offset="0.16" stop-color="#f2a56e"/>
        <stop offset="0.28" stop-color="#f6c08d"/>
        <stop offset="0.34" stop-color="#5e93a6"/>
        <stop offset="0.55" stop-color="#2b7d99"/>
        <stop offset="1" stop-color="#1d5f8c"/>
      </linearGradient>
    </defs>
    <path d="M0 0 H1200 V1040 C1050 760 620 560 0 600 Z" fill="url(#sceneGradient)"/>
    <path d="M620 40 H1200 V620 C1000 560 780 470 620 380 Z" fill="#e9ecef" opacity="0.55"/>
  </svg>

  <div class="brand-mark"><span class="dot"></span>HarborLoop</div>

  <div class="tablet-shadow"></div>
  <div class="tablet">
    <div class="tablet-screen" role="img" aria-label="Software screen showing the cruise calendar month view with ship arrivals listed by day"></div>
  </div>

  <h1 class="headline">The Operating<br>System for Shore<br>Excursions</h1>

  <div class="values-tag">Key Values</div>

  <div class="value v-revenue">
    <svg width="130" height="130" viewBox="0 0 130 130" aria-hidden="true">
      <circle cx="72" cy="76" r="44" fill="var(--accent-blue)"/>
      <circle cx="62" cy="62" r="46" fill="#fff" stroke="#fff" stroke-width="0"/>
      <circle cx="62" cy="62" r="46" fill="none" stroke="var(--ink-navy)" stroke-width="0"/>
      <circle cx="62" cy="62" r="56" fill="none" stroke="#fff" stroke-width="4" stroke-dasharray="250 60"/>
      <text x="62" y="82" text-anchor="middle" font-family="Roboto, sans-serif" font-size="58" fill="var(--accent-blue)">$</text>
      <path d="M10 40 l6 -16 l12 10" fill="none" stroke="#fff" stroke-width="4"/>
    </svg>
    <div class="value-label">Maximize Revenue</div>
  </div>

  <div class="value v-control">
    <svg width="130" height="130" viewBox="0 0 130 130" aria-hidden="true">
      <path d="M52 8 L94 22 V60 C94 92 72 112 52 122 C32 112 10 92 10 60 V22 Z" fill="none" stroke="#fff" stroke-width="4"/>
      <circle cx="82" cy="84" r="40" fill="var(--accent-blue)"/>
      <circle cx="82" cy="84" r="20" fill="none" stroke="#fff" stroke-width="4"/>
      <circle cx="82" cy="84" r="7" fill="#fff"/>
    </svg>
    <div class="value-label">Operational<br>Control</div>
  </div>

  <div class="value v-bookings">
    <svg width="130" height="130" viewBox="0 0 130 130" aria-hidden="true">
      <circle cx="66" cy="98" r="30" fill="var(--accent-blue)"/>
      <rect x="16" y="18" width="98" height="96" rx="4" fill="none" stroke="#fff" stroke-width="4"/>
      <line x1="16" y1="40" x2="114" y2="40" stroke="#fff" stroke-width="4"/>
      <g fill="none" stroke="#fff" stroke-width="3">
        <rect x="28" y="52" width="14" height="12"/><rect x="50" y="52" width="14" height="12"/><rect x="72" y="52" width="14" height="12"/><rect x="94" y="52" width="12" height="12"/>
        <rect x="28" y="74" width="14" height="12"/><rect x="72" y="74" width="14" height="12"/><rect x="94" y="74" width="12" height="12"/>
        <rect x="28" y="94" width="14" height="12"/><rect x="50" y="94" width="14" height="12"/><rect x="72" y="94" width="14" height="12"/>
        <path d="M50 80 l6 6 l10 -12"/>
        <path d="M36 10 v16 M58 10 v16 M80 10 v16 M102 10 v16"/>
      </g>
    </svg>
    <div class="value-label">Simplify Bookings</div>
  </div>

  <div class="value v-management">
    <svg width="150" height="140" viewBox="0 0 150 140" aria-hidden="true">
      <circle cx="98" cy="66" r="44" fill="var(--accent-blue)"/>
      <circle cx="98" cy="66" r="24" fill="none" stroke="#fff" stroke-width="5" stroke-dasharray="8 5"/>
      <circle cx="98" cy="66" r="12" fill="#fff"/>
      <circle cx="40" cy="58" r="14" fill="none" stroke="#fff" stroke-width="5" stroke-dasharray="6 4"/>
      <circle cx="66" cy="18" r="12" fill="none" stroke="#fff" stroke-width="5" stroke-dasharray="6 4"/>
      <path d="M14 118 C30 100 48 100 66 108 H96 C104 108 104 118 96 118 H70 M20 132 H94 L130 108" fill="none" stroke="#fff" stroke-width="5" stroke-linejoin="round"/>
    </svg>
    <div class="value-label">Smarter<br>Management</div>
  </div>

  <div class="value v-future">
    <svg width="150" height="140" viewBox="0 0 150 140" aria-hidden="true">
      <circle cx="100" cy="90" r="42" fill="var(--accent-blue)"/>
      <path d="M70 22 L120 40 V76 C120 108 96 126 70 136 C44 126 20 108 20 76 V40 Z" fill="none" stroke="#fff" stroke-width="4"/>
      <path d="M70 38 L106 50 V78 C106 102 90 116 70 124 C50 116 34 102 34 78 V50 Z" fill="none" stroke="#fff" stroke-width="3" stroke-dasharray="6 5"/>
      <path d="M70 70 C62 84 58 90 58 96 a12 12 0 0 0 24 0 C82 90 78 84 70 70 Z" fill="none" stroke="#fff" stroke-width="4"/>
      <circle cx="118" cy="28" r="24" fill="none" stroke="#fff" stroke-width="4"/>
      <path d="M106 28 l8 8 l16 -16" fill="none" stroke="#fff" stroke-width="5"/>
    </svg>
    <div class="value-label">Future-Proof</div>
  </div>

  <div class="deco-circle"></div>
  <div class="closing-arc"></div>

  <p class="tagline">Cruise Smarter. Operate<br>Stronger. Grow Faster.</p>
  <p class="wordmark">HarborLoop</p>
</div>
</body>
</html>
```